Letterhead Design Project (logo provided)

We are a legal services provider company called VRN Legal based in the UK and would like some letterhead paper designed.

The design should use the attached logo, and should use the colors feature in the logo (along with blacks and/or greys).

The background paper must be white - and A4 size.

The letterhead should be provided in both .pdf and .doc (or .odf) formats.

Target Market(s)

Customers and clients for legal services

Industry/Entity Type

Legal

Requirements
Must have
• The header must include the following information:

Business name - VRN Legal LLP
Office address - Larchmead Court, Wallingford, Oxfordshire OX10 4TL, United Kingdom
Telephone - +44 (0)1491 736480
Email - mail@ [domain given below]
Website: www.vrnlegal-example.com

The footer must include the following information:

Registered office address - 14 Alder Row, Brindlecote, Wallingford, Oxfordshire OX10 6QD, United Kingdom
Companies House registration number - OC718463
VAT registration number - GB 417386205

```html
<!DOCTYPE html>
<html lang="en">
<head>
<meta charset="utf-8">
<title>VRN Legal LLP – Letterhead</title>
<link rel="stylesheet" href="https://fonts.googleapis.com/css2?family=Source+Sans+3:wght@400;600&display=swap">
<style>
  :root {
    --backdrop: #ececec;
    --paper: #ffffff;
    --brand-blue: #3a67a8;
    --brand-green: #45a64b;
    --text-grey: #6b6b6b;
    --text-dark: #4a4a4a;
  }
  * { box-sizing: border-box; margin: 0; padding: 0; }
  html, body {
    width: 1200px;
    height: 911px;
    overflow: hidden;
    background: var(--backdrop);
    font-family: "Source Sans 3", "Myriad Pro", Arial, sans-serif;
  }
  .letterhead {
    position: absolute;
    left: 302px;
    top: 26px;
    width: 596px;
    height: 843px;
    background: var(--paper);
    box-shadow: 0 2px 10px rgba(0,0,0,0.12);
    overflow: hidden;
  }
  .sender {
    position: absolute;
    top: 34px;
    right: 36px;
    text-align: right;
    font-size: 8px;
    line-height: 1.25;
    color: var(--text-grey);
  }
  .sender .firm-name { font-weight: 600; color: var(--text-dark); }
  .contact-list {
    list-style: none;
    margin-top: 6px;
  }
  .contact-list li {
    display: flex;
    justify-content: flex-end;
    align-items: center;
    gap: 4px;
  }
  .contact-list svg { width: 7px; height: 7px; flex: none; }
  .brand {
    position: absolute;
    top: 150px;
    left: 40px;
    display: flex;
    align-items: center;
    gap: 8px;
  }
  .brand-dot {
    width: 14px;
    height: 14px;
    border-radius: 50%;
    background: var(--brand-green);
  }
  .brand-name {
    font-size: 34px;
    font-weight: 400;
    letter-spacing: 1px;
    color: var(--brand-blue);
  }
  .registered {
    position: absolute;
    right: 36px;
    bottom: 118px;
    text-align: right;
    font-size: 8px;
    line-height: 1.3;
    color: var(--text-grey);
  }
  .corner-band {
    position: absolute;
    left: 96px;
    bottom: 0;
    width: 180px;
    height: 28px;
    background: var(--brand-green);
  }
</style>
</head>
<body>
  <main class="letterhead">
    <header class="sender">
      <p class="firm-name">VRN Legal LLP</p>
      <p>Larchmead Court, Wallingford,</p>
      <p>Oxfordshire OX10 4TL,</p>
      <p>United Kingdom</p>
      <ul class="contact-list">
        <li>
          <svg viewBox="0 0 10 10" aria-hidden="true"><path d="M2 1 L4 1 L4.6 3.4 L3.3 4.3 Q4.4 6.2 5.7 6.7 L6.6 5.4 L9 6 L9 8 Q9 9 8 9 Q1 8.5 1 2 Q1 1 2 1 Z" fill="var(--brand-green)"/></svg>
          <span>+44 (0)1491 736480</span>
        </li>
        <li>
          <svg viewBox="0 0 10 10" aria-hidden="true"><rect x="0.5" y="2" width="9" height="6.5" fill="var(--brand-green)"/><path d="M0.8 2.3 L5 5.6 L9.2 2.3" stroke="#fff" stroke-width="0.8" fill="none"/></svg>
          <span>mail@vrnlegal-example.com</span>
        </li>
        <li>
          <svg viewBox="0 0 10 10" aria-hidden="true"><circle cx="5" cy="5" r="4.5" fill="var(--brand-green)"/></svg>
          <span>www.vrnlegal-example.com</span>
        </li>
      </ul>
    </header>

    <div class="brand">
      <span class="brand-name">VRN Legal</span>
      <span class="brand-dot" aria-hidden="true"></span>
    </div>

    <footer class="registered">
      <p>Registered office address:</p>
      <p>14 Alder Row, Brindlecote, Wallingford, Oxfordshire OX10 6QD, United Kingdom</p>
      <p>Companies House registration number - OC718463</p>
      <p>VAT registration number - GB 417386205</p>
    </footer>

    <div class="corner-band" aria-hidden="true"></div>
  </main>
</body>
</html>
```